Design for Marketing Consulting Agency - Please see attachments

Looking for a very simple site - 3-5 pages, one with a portfolio page to showcase our work where we can leave comments on it. Looking for modern/clean/impactful design to represent our brand. Here is example of what I like: https://www.norvika.example/en-us/ logo and mood board and copy for website (minus the portfolio). Prefer black/gray/white with pops of color/imagery that come from the logo. Prefer dark hero, more white and pops of the orange and red for the rest of the site.

Target Market(s)

Small to medium size businesses

Font styles to use
Sans Serif

Colors

Designer to choose only greyscale colors for use in the design.

Requirements
Must have
• Please see mood board. Prefer mostly black/white site with pops of color and imagery.
Nice to have
• Sample portfolio page?
Should not have
• Don't make it look 'futuristic' . Try to make it modern and clean.

```html
<!DOCTYPE html>
<html lang="en">
<head>
<meta charset="utf-8">
<title>Brightline Marketing</title>
<link rel="stylesheet" href="https://fonts.googleapis.com/css2?family=Comfortaa:wght@400;600;700&family=Righteous&display=swap">
<style>
:root{
  --gold:#f5a823;
  --gold-deep:#c8951c;
  --ink:#2c2c2c;
  --text:#555;
  --dark:#363636;
  --dark-2:#2d2d2d;
  --white:#fff;
  --team-bg:#f2f2f2;
  --welcome-bg:#faf5ec;
  --red:#e2401c;
}
*{margin:0;padding:0;box-sizing:border-box}
html,body{width:1200px;height:3766px;overflow:hidden}
body{position:relative;background:var(--white);font-family:"Comfortaa",sans-serif;color:var(--ink)}
a{text-decoration:none}
.abs{position:absolute}
.display{font-family:"Righteous",sans-serif;font-weight:400}
.btn{position:absolute;display:flex;align-items:center;justify-content:center;background:var(--gold);color:var(--ink);font-family:"Righteous",sans-serif;font-size:13px;border-radius:2px;text-decoration:none}
.btn::after{content:"";position:absolute;right:4px;bottom:4px;border-left:6px solid transparent;border-bottom:6px solid var(--ink)}

/* header & hero */
.hero{left:0;top:0;width:1200px;height:675px;background:linear-gradient(180deg,#f6dcc7 0%,#f0cfb6 35%,#c9877a 70%,#8a6a5e 100%)}
.brand{display:flex;align-items:center;gap:10px}
.brand-square{width:40px;height:40px;background:var(--gold-deep)}
.brand-name{font-family:"Comfortaa",sans-serif;font-weight:600;font-size:15px;line-height:15px;color:var(--ink);text-transform:uppercase}
.nav a{position:absolute;top:28px;font-family:"Righteous",sans-serif;font-size:13px;color:var(--ink)}
.hero-mark{left:0;width:1200px;top:300px;text-align:center;font-family:"Righteous",sans-serif;font-size:96px;color:var(--gold-deep)}
.hero-title{left:0;width:1200px;top:528px;text-align:center;font-size:41px;line-height:50px;color:var(--white)}

/* welcome */
.welcome-panel{left:60px;top:751px;width:1079px;height:222px;background:var(--welcome-bg);border-radius:12px}
.welcome-title{left:117px;top:796px;font-size:32px;line-height:41px;color:var(--ink)}
.welcome-title span{color:var(--gold)}
.welcome-text{left:412px;top:800px;width:645px;font-size:12.5px;line-height:21.6px;color:var(--text)}

/* packages */
.packages-band{left:0;top:1049px;width:1200px;height:649px;background:linear-gradient(135deg,var(--dark) 0%,var(--dark-2) 100%)}
.section-title{font-size:32px;color:var(--gold);text-align:center}
.packages-title{left:0;width:1200px;top:1116px}
.packages-sub{left:0;width:1200px;top:1170px;text-align:center;font-size:12px;font-weight:700;color:var(--white)}
.card{position:absolute;top:1215px;width:345px;height:561px}
.card-img{width:345px;height:232px}
.card-body{padding:24px 29px 0}
.card h3{font-family:"Righteous",sans-serif;font-weight:400;font-size:17px;color:var(--ink)}
.card .price{font-weight:700;font-size:16px;color:var(--red);margin-top:10px}
.card .label{font-weight:700;font-size:12px;margin-top:18px;color:#444}
.card p,.card li{font-size:12px;line-height:19px;color:#444}
.card ul{list-style:none;margin-top:4px}
.card li{padding-left:10px;text-indent:-10px}
.card .btn{left:30px;bottom:31px;width:148px;height:34px}
.card-site{left:60px;background:#fdf4e6}
.card-brand{left:427px;background:#fcefec}
.card-extra{left:795px;background:#eeeeee}

/* about */
.about-art{left:60px;top:1868px;width:540px;height:266px;border-radius:40px 0 0 40px;background:linear-gradient(90deg,#fbe0e0 0%,#f6f0f4 50%,#fbe9cf 100%)}
.about-title{left:659px;top:1865px;font-size:32px;color:var(--gold)}
.about-text{left:659px;top:1916px;width:460px;font-size:12.5px;line-height:21.6px;color:var(--text)}

/* team */
.team-band{left:60px;top:2210px;width:1140px;height:530px;background:var(--team-bg);border-top-left-radius:88px}
.team-title{left:120px;top:2278px;font-size:32px;color:var(--gold)}
.team-text{left:120px;top:2324px;width:680px;font-size:12.5px;font-weight:700;line-height:22px;color:#444}
.member{position:absolute;top:2393px;width:225px;height:273px;border-radius:0 0 0 18px;overflow:hidden}
.member span{position:absolute;left:0;bottom:0;width:100%;height:44px;line-height:40px;text-align:center;font-family:"Righteous",sans-serif;font-size:17px;color:var(--white);background:linear-gradient(0deg,rgba(0,0,0,.55),rgba(0,0,0,0))}

/* testimonials */
.clients-band{left:0;top:2740px;width:1200px;height:515px;background:linear-gradient(135deg,var(--dark) 0%,var(--dark-2) 100%)}
.clients-title{left:0;width:1200px;top:2808px}
.quote{left:285px;top:2884px;width:630px;text-align:center;font-size:13.5px;line-height:24px;color:#e8e8e8}
.client{left:0;width:1200px;top:3024px;display:flex;justify-content:center;align-items:center;gap:14px;font-family:"Righteous",sans-serif;font-size:17px;color:var(--white)}
.client i{width:50px;height:50px;border-radius:50%;background:#222}
.logo-word{position:absolute;top:3146px;width:220px;text-align:center;font-family:"Righteous",sans-serif;font-size:30px;color:var(--white)}

/* cta */
.cta{left:0;width:1200px;top:3322px;text-align:center;font-size:32px;color:var(--gold)}
.cta a{color:var(--ink);border-bottom:2px solid var(--ink);padding-bottom:6px;margin-left:6px}

/* footer */
.footer{left:0;top:3447px;width:1200px;height:319px;background:var(--dark)}
.follow{left:60px;top:3578px;font-family:"Righteous",sans-serif;font-size:16px;color:var(--white)}
.social{position:absolute;top:3622px;width:32px;height:32px;background:#4a4a4a}
.social.first{background:var(--gold)}
.foot-head{position:absolute;top:3502px;font-family:"Righteous",sans-serif;font-weight:400;font-size:17px;color:var(--white)}
.foot-list{position:absolute;top:3542px;list-style:none}
.foot-list li{font-size:11px;line-height:26px;color:#ddd;position:relative;padding-left:15px}
.foot-list li::before{content:"";position:absolute;left:0;top:11px;width:4px;height:4px;background:var(--gold)}
.contact-row{position:absolute;left:886px;display:flex;align-items:center;gap:14px;font-size:11px;line-height:15px;color:#eee}
.contact-row .ico{width:32px;height:32px;background:var(--gold);display:flex;align-items:center;justify-content:center;flex:none}
.contact-row a{color:#eee;text-decoration:underline}
.foot-rule{left:60px;top:3720px;width:1080px;height:1px;background:#4c4c4c}
.copyright{left:0;width:1200px;top:3735px;text-align:center;font-size:10px;font-weight:700;color:#eee}
.copyright span{color:var(--gold)}
</style>
</head>
<body>

<!-- Hero -->
<section class="abs hero" role="img" aria-label="Photograph of a suspension bridge over a bay at sunset"></section>
<header>
  <div class="abs brand" style="left:60px;top:17px">
    <i class="brand-square"></i>
    <span class="brand-name">Brightline<br>Marketing</span>
  </div>
  <nav class="nav">
    <a style="left:431px" href="#">Packages</a>
    <a style="left:532px" href="#">Portfolio</a>
    <a style="left:631px" href="#">About Us</a>
    <a style="left:731px" href="#">Contact Us</a>
  </nav>
  <a class="btn" style="left:1020px;top:20px;width:119px;height:36px" href="#">Get Started</a>
</header>
<div class="abs hero-mark">Brightline</div>
<h1 class="abs display hero-title">We Deliver Simple, Clear, &amp; Impactful<br>Messaging and Designs.</h1>

<!-- Welcome -->
<div class="abs welcome-panel"></div>
<h2 class="abs display welcome-title"><span>Welcome To</span><br>Brightline<br>Marketing</h2>
<p class="abs welcome-text">It's an unfortunate fact – many business owners overthink their marketing. They try to be overly creative or wordy, resulting in empty statements, confused consumers, and lost revenue opportunities. Brightline Marketing has a simple, thorough process that we use to understand your customer base and their unique pain points. We then develop clear, impactful messaging and beautiful designs that resonate with your audience, differentiate you in your market, and drive sales.</p>

<!-- Packages -->
<section class="abs packages-band" role="img" aria-label="Dark grey band with a soft diamond pattern"></section>
<h2 class="abs display section-title packages-title">Our Packages</h2>
<p class="abs packages-sub">We also are offer special discount packages for non-profits. Please Inquire</p>

<article class="card card-site">
  <div class="card-img" role="img" aria-label="Website mockups for a restaurant on a yellow background" style="background:linear-gradient(135deg,#fcd27a,#f6b946)"></div>
  <div class="card-body">
    <h3>Website &amp; Messaging Facelift -</h3>
    <p class="price">$3000 -$4000</p>
    <p class="label">Meetings Necessary:</p>
    <p><b>4-5 hours</b></p>
    <p class="label" style="margin-top:10px">The Output:</p>
    <ul><li>- Two homepage mockups.</li><li>- One mood board.</li><li>- Two versions of value proposition messaging – x words.</li></ul>
  </div>
  <a class="btn" href="#">See Case Study</a>
</article>

<article class="card card-brand">
  <div class="card-img" role="img" aria-label="Business card mockup on a copper surface" style="background:linear-gradient(135deg,#c9764a,#a85a34)"></div>
  <div class="card-body">
    <h3>Simple Brand Rebuild -</h3>
    <p class="price">$5000-$6000</p>
    <p class="label">Meetings Necessary:</p>
    <p><b>6-7 hours</b></p>
    <p class="label" style="margin-top:10px">The Output:</p>
    <ul><li>- 5 logo concepts</li><li>- Two homepage mockups</li><li>- One brand storyboard</li><li>- Two versions of value proposition messaging</li></ul>
  </div>
  <a class="btn" href="#">See Case Study</a>
</article>

<article class="card card-extra">
  <div class="card-img" role="img" aria-label="City street at night with illuminated billboards" style="background:linear-gradient(135deg,#1d3a44,#2c6a6a 50%,#1a2228)"></div>
  <div class="card-body">
    <h3>Additional Services Offered -</h3>
    <p class="price" style="font-weight:400">(Charged Hourly)</p>
    <ul style="margin-top:52px"><li>- Strategic Consulting on Growth Strategies and Building Teams</li><li>- Trade Show Management &amp; Booth Designs</li><li>- Email Marketing Campaigns</li><li>- Digital Marketing Campaigns</li></ul>
  </div>
  <a class="btn" href="#">See Case Study</a>
</article>

<!-- About -->
<div class="abs about-art" role="img" aria-label="Illustration of two people working with marketing icons"></div>
<h2 class="abs display about-title">Who Are We?</h2>
<p class="abs about-text">Brightline Marketing is a Marketing Agency that delivers a breadth of services from brand/rebrand, strategy, design, and web to digital and print marketing campaigns and trade shows. We bring over 20 years of experience in marketing for both B2B to B2C organizations ranging from 5M to over 200M. We're passionate. We're poignant. We know what you're trying to say, and so will your customers.</p>
<a class="btn" style="left:661px;top:2092px;width:163px;height:35px" href="#">Learn More About</a>

<!-- Team -->
<section class="abs team-band"></section>
<h2 class="abs display team-title">Our Team</h2>
<p class="abs team-text">Brightline Marketing is run and managed by Renata Vale. It has a team of experts from content creation to graphic design and digital marketing.</p>
<figure class="member" style="left:120px;background:linear-gradient(180deg,#6b4a3a,#2a2222)" role="img" aria-label="Portrait of Renata Vale"><span>Renata Vale</span></figure>
<figure class="member" style="left:365px;background:linear-gradient(180deg,#4a4a48,#1f1f1f)" role="img" aria-label="Portrait of Owen Marsh"><span>Owen Marsh</span></figure>
<figure class="member" style="left:611px;background:linear-gradient(180deg,#a88a6e,#5c4434)" role="img" aria-label="Portrait of Ida Frost"><span>Ida Frost</span></figure>
<figure class="member" style="left:855px;background:linear-gradient(180deg,#8c8a84,#3c3c3a)" role="img" aria-label="Portrait of Leo Brandt"><span>Leo Brandt</span></figure>

<!-- Testimonials -->
<section class="abs clients-band" role="img" aria-label="Dark grey band with a soft diamond pattern"></section>
<h2 class="abs display section-title clients-title">What Happy Clients Say</h2>
<p class="abs quote">"Lorem ipsum dolor sit amet, consectetuer adipiscing elit, sed diam nonummy nibh euismod tincidunt ut laoreet dolore magna aliquam erat volutpat. Ut wisi enim ad minim veniam, quis nostrud exerci tation ullamcorper suscipit lobortis nisl ut aliquip ex ea commodo consequat. Duis autem vel eum iriure dolor in hendrerit in vulputate velit esse molestie consequat."</p>
<div class="abs client"><i></i>Tonehall</div>
<div class="logo-word" style="left:99px">Quillmark</div>
<div class="logo-word" style="left:378px">Vectora</div>
<div class="logo-word" style="left:638px">Halden</div>
<div class="logo-word" style="left:891px">Ridgeway</div>

<!-- CTA -->
<p class="abs display cta">Get Started With Brightline Marketing. <a href="#">Let's Talk?</a></p>

<!-- Footer -->
<footer class="abs footer"></footer>
<div class="abs brand" style="left:60px;top:3508px">
  <i class="brand-square"></i>
  <span class="brand-name" style="color:#fff">Brightline<br>Marketing</span>
</div>
<p class="abs follow">Follow Us On:</p>
<a class="social first" style="left:60px" href="#" aria-label="Social profile 1"></a>
<a class="social" style="left:101px" href="#" aria-label="Social profile 2"></a>
<a class="social" style="left:142px" href="#" aria-label="Social profile 3"></a>
<a class="social" style="left:183px" href="#" aria-label="Social profile 4"></a>

<h3 class="foot-head" style="left:355px">Company</h3>
<ul class="foot-list" style="left:355px"><li>About Us</li><li>Packages</li><li>Portfolio</li><li>Contact Us</li></ul>
<h3 class="foot-head" style="left:571px">Packages</h3>
<ul class="foot-list" style="left:571px"><li>Website &amp; Messaging Facelift</li><li>Simple Brand Rebuild</li><li>Additional Services</li></ul>
<h3 class="foot-head" style="left:884px">Contact Details</h3>

<div class="contact-row" style="top:3546px">
  <span class="ico"><svg width="14" height="18" viewBox="0 0 14 18"><path d="M7 0a7 7 0 0 0-7 7c0 5 7 11 7 11s7-6 7-11a7 7 0 0 0-7-7z" fill="#2c2c2c"/><circle cx="7" cy="7" r="2.6" fill="#f5a823"/></svg></span>
  <span>123 Building Name, Area Name,<br>City, Country - Zipcode</span>
</div>
<div class="contact-row" style="top:3586px">
  <span class="ico"><svg width="16" height="16" viewBox="0 0 16 16"><path d="M3 1l3 3-2 2a10 10 0 0 0 6 6l2-2 3 3-2 2C7 15 1 9 1 3z" fill="#2c2c2c"/></svg></span>
  <span>(123) 4567 890</span>
</div>
<div class="contact-row" style="top:3626px">
  <span class="ico"><svg width="16" height="12" viewBox="0 0 16 12"><rect width="16" height="12" fill="#2c2c2c"/><path d="M0 0l8 6 8-6" stroke="#f5a823" stroke-width="1.4" fill="none"/></svg></span>
  <a href="#">info@brightlinemarketing.example</a>
</div>

<div class="abs foot-rule"></div>
<p class="abs copyright">© <span>BRIGHTLINE MARKETING</span> - 2022. All Rights Reserved.</p>

</body>
</html>
```